2 banners on the outside wall of the hall

Banner 1:
Kalvamo specializes in the planning, construction, and maintenance of high-quality pond systems, particularly swimming ponds, natural pools, garden ponds, koi ponds, streams, and waterfalls. Learn more at www.kalvamo.de
The following data should be included:
Planning and construction of swimming ponds and natural pools, as well as garden ponds and koi ponds
100% organic
Individually planned
Over 20 years of experience
04271 6632907
www.kalvamo.de
“Logo-Kalvamo”
Banner 2:
Lumo-Grün is the online shop for high-quality aquatic plants for ponds and aquariums.
More information at https://lumo-gruen.de
Online shop for pond plants and water lilies, as well as aquarium plants and accessories
Over 400 plant species
Top gardener quality
Secure packaging & fast shipping
04271 6632906
www.lumo-gruen. de
“Logo Lumo green”
Here's roughly what we envision:
The designs for each banner should be clearly visible and include everything needed, without appearing cluttered. In other words, it should be immediately clear what the banner is about.
We should also be made aware of our unique selling points and advantages.
It is important that the banners also harmonize visually with each other.
We liked the banner image in the attachment and it serves as inspiration.
The banner print data is produced as follows:
• Banner size: Width x Height: 3880 mm x 1880 mm
• Material: Mesh banner, PVFormat: PDF (X-3:2000)
• Fonts: converted into paths
• Trim allowance: +2 mm all around
• Color space: CMYK
• Resolution: 72 dpi (recommended) at 1:1 resolution
Look and feel
Each slider illustrates characteristics of the customer's brand and the style your logo design should communicate.

```html
<!DOCTYPE html>
<html lang="en">
<head>
<meta charset="utf-8">
<title>Kalvamo Banner</title>
<link href="https://fonts.googleapis.com/css2?family=Archivo+Narrow:wght@700&family=Archivo:wght@500;600&display=swap" rel="stylesheet">
<style>
:root{
  --bg:#dddddd;
  --brand-blue:#2a5f88;
  --brand-green:#7dc242;
  --ink:#1a1a1a;
  --white:#ffffff;
}
html,body{margin:0;padding:0;width:1200px;height:1200px;overflow:hidden;background:var(--bg);}
.banner{position:absolute;left:74px;top:345px;width:1052px;height:510px;background:var(--white);overflow:hidden;}
.headline-band{position:absolute;left:0;top:0;width:1052px;height:130px;background:var(--brand-blue);}
.headline{position:absolute;left:35px;top:26px;margin:0;color:var(--white);font-family:"Archivo Narrow",sans-serif;font-weight:700;font-size:36px;line-height:47px;letter-spacing:0;text-transform:uppercase;white-space:nowrap;}
.usp-list{position:absolute;left:36px;top:140px;margin:0;padding:0;list-style:none;font-family:Archivo,sans-serif;font-weight:600;font-size:28px;line-height:31px;color:var(--ink);}
.usp-list li{position:relative;padding-left:35px;margin-bottom:7px;}
.usp-list svg{position:absolute;left:0;top:5px;width:23px;height:23px;}
.brand{position:absolute;left:36px;top:298px;width:300px;}
.brand-name{font-family:Archivo,sans-serif;font-weight:600;font-size:64px;line-height:70px;color:var(--brand-blue);letter-spacing:-1px;white-space:nowrap;}
.contact-band{position:absolute;left:0;top:392px;width:372px;height:118px;background:var(--brand-blue);}
.phone{position:absolute;left:36px;top:10px;font-family:Archivo,sans-serif;font-weight:600;font-size:42px;line-height:50px;color:var(--brand-green);white-space:nowrap;}
.web{position:absolute;left:36px;top:58px;font-family:Archivo,sans-serif;font-weight:500;font-size:39px;line-height:46px;color:var(--white);white-space:nowrap;}
.pond-photo{position:absolute;left:372px;top:130px;width:680px;height:380px;
  background:linear-gradient(180deg,#4f8fd4 0%,#9cc3ea 38%,#5f8a3e 55%,#6f9ab8 72%,#6a8a44 100%);}
</style>
</head>
<body>
<div class="banner">
  <div class="headline-band">
    <h1 class="headline">Planning and construction of swimming ponds and<br>natural pools, as well as garden ponds and koi ponds</h1>
  </div>
  <ul class="usp-list">
    <li><svg viewBox="0 0 24 24"><circle cx="11" cy="12" r="9" fill="none" stroke="#2a5f88" stroke-width="2.4"/><path d="M6.5 12l4 4 11-12" fill="none" stroke="#2a5f88" stroke-width="3"/></svg>100% organic</li>
    <li><svg viewBox="0 0 24 24"><circle cx="11" cy="12" r="9" fill="none" stroke="#2a5f88" stroke-width="2.4"/><path d="M6.5 12l4 4 11-12" fill="none" stroke="#2a5f88" stroke-width="3"/></svg>Individually planned</li>
    <li><svg viewBox="0 0 24 24"><circle cx="11" cy="12" r="9" fill="none" stroke="#2a5f88" stroke-width="2.4"/><path d="M6.5 12l4 4 11-12" fill="none" stroke="#2a5f88" stroke-width="3"/></svg>Over 20 years of<br>experience</li>
  </ul>
  <div class="brand">
    <div class="brand-name">Kalvamo</div>
  </div>
  <div class="contact-band">
    <div class="phone">04271 6632907</div>
    <div class="web">www.kalvamo.de</div>
  </div>
  <div class="pond-photo" role="img" aria-label="Natural swimming pond with wooden jetty, reeds, trees and blue summer sky"></div>
</div>
</body>
</html>
```